Financial Planning Firm looking for stationary design using new logo

Need stationary design using our new logo. We are a financial planning firm focused on the planning needs of retirees. Design should incorporate our new logo and its colors. The design should communicate a feeling of stability and security.
Have attached our new logo, as well as our old stationary for reference, letterhead, envelope and business card (but don't rely on for your design). Although the following disclosure must be present on all items "Securities and advisory services offered through Valdimo Advisor Networks LLC, member QUBEX/DLWT. Valdimo is under seperate ownership from any other named entity." in minimum 8 size font. you can see our old stationary for idea of disclosure placement. The business card (front and back) is in the middle of our letterhead sample if it is hard to tell.
Financial

```html
<!DOCTYPE html>
<html lang="en">
<head>
<meta charset="utf-8">
<title>Envelope Back – Marlow T. Hensley Financial Group</title>
<link rel="stylesheet" href="https://fonts.googleapis.com/css2?family=EB+Garamond:wght@400&display=swap">
<style>
  :root {
    --page-bg: #ffffff;
    --paper: #fdfdfd;
    --fold-line: #3a3a3a;
    --brand-blue: #3e5f7c;
  }
  html, body {
    margin: 0;
    padding: 0;
    width: 1200px;
    height: 849px;
    overflow: hidden;
    background: var(--page-bg);
  }
  .canvas {
    position: relative;
    width: 1200px;
    height: 849px;
  }
  .envelope-back {
    position: absolute;
    left: 145px;
    top: 224px;
    width: 910px;
    height: 400px;
    background: var(--paper);
  }
  .envelope-back svg {
    position: absolute;
    inset: 0;
    width: 100%;
    height: 100%;
  }
  .return-address {
    position: absolute;
    left: 0;
    right: 0;
    top: 310px;
    margin: 0;
    text-align: center;
    font-family: "EB Garamond", Garamond, serif;
    font-style: normal;
    font-size: 13px;
    line-height: 15.5px;
    color: var(--brand-blue);
  }
  .return-address .firm-name {
    display: block;
    font-size: 13.5px;
    letter-spacing: 0.06em;
    word-spacing: 0.45em;
  }
</style>
</head>
<body>
  <main class="canvas">
    <section class="envelope-back" aria-label="Envelope back">
      <svg viewBox="0 0 888 390" preserveAspectRatio="none" aria-hidden="true">
        <rect class="envelope-edge" x="0.5" y="0.5" width="887" height="389" fill="none" stroke="var(--fold-line)" stroke-width="0.8"/>
        <path class="flap-fold" d="M0,0 L247,172 C330,228 390,254 453,254 C520,254 582,224 645,177 L888,0" fill="none" stroke="var(--fold-line)" stroke-width="0.7"/>
        <path class="side-fold" d="M0,390 L247,172 M888,390 L645,177" fill="none" stroke="var(--fold-line)" stroke-width="0.7"/>
      </svg>
      <address class="return-address">
        <span class="firm-name">MARLOW T. HENSLEY FINANCIAL GROUP, LLC</span>
        4420 Harbor Avenue, Suite 310,<br>
        Kirkland, WA 98033
      </address>
    </section>
  </main>
</body>
</html>
```